Camp Flyer

We are hosting a camp over the last week of October. We would like a high res file for a flyer that we can get printed. Double sided would be great but i would also like a version that is only 1 side that can be sent out via email to our database and also posted on our social media platforms.

The text that should be included
Mid Term Camp
26th - 30th of October
9am - 3pm
800 aed

Let your star shine bright!
Daily speech and confidence building classes, music & movement, song, arts & crafts, fine motor development and right brain training!

Special performance of the Patchwork Fox from Quillby Theatre Group (Wednesday).

Pixelnook Camp photo gallery updated daily!

Limited Spaces Available

register@wrenbloom.ae or 043192764/ 0529316472
www.wrenbloom.ae

- I have a larger file of this photo it would just not allow me to attach the large file to this brief.

For details on the theatre show please look at www.quillbytheatre.com - please use their patchwork fox and logo

```html
<!DOCTYPE html>
<html lang="en">
<head>
<meta charset="utf-8">
<title>Mid Term Camp Flyer</title>
<link href="https://fonts.googleapis.com/css2?family=Chewy&family=Roboto+Condensed:wght@400&family=Arimo:wght@400;700&display=swap" rel="stylesheet">
<style>
  :root {
    --sky: #2ea5df;
    --sky-deep: #1b86c7;
    --sky-ring: #1e93d2;
    --sky-pale: #a8dcf0;
    --pink: #e5197f;
    --green: #7cb53a;
    --white: #ffffff;
    --ink: #2b3440;
  }
  html, body {
    margin: 0;
    padding: 0;
    width: 964px;
    height: 1200px;
    overflow: hidden;
    background: var(--white);
  }
  .flyer {
    position: relative;
    width: 964px;
    height: 1200px;
    overflow: hidden;
    background: var(--sky);
  }
  .flyer-shapes {
    position: absolute;
    inset: 0;
  }
  .camp-title {
    position: absolute;
    left: 0;
    right: 0;
    top: 46px;
    margin: 0;
    text-align: center;
    font-family: "Chewy", "Comic Sans MS", cursive;
    font-weight: 400;
    font-size: 82px;
    line-height: 96px;
    letter-spacing: 3px;
    color: var(--pink);
    text-shadow:
      -4px -4px 0 var(--white), 4px -4px 0 var(--white),
      -4px 4px 0 var(--white), 4px 4px 0 var(--white),
      0 5px 0 var(--white), 0 -5px 0 var(--white),
      5px 0 0 var(--white), -5px 0 0 var(--white),
      7px 9px 0 rgba(40, 30, 60, 0.45);
    transform: translateX(40px);
  }
  .camp-dates {
    position: absolute;
    left: 0;
    right: 0;
    top: 140px;
    margin: 0;
    text-align: center;
    font-family: "Chewy", "Comic Sans MS", cursive;
    font-size: 50px;
    line-height: 58px;
    color: var(--pink);
    text-shadow:
      -3px -3px 0 var(--white), 3px -3px 0 var(--white),
      -3px 3px 0 var(--white), 3px 3px 0 var(--white),
      0 4px 0 var(--white), 0 -4px 0 var(--white),
      4px 0 0 var(--white), -4px 0 0 var(--white);
    transform: translateX(40px) rotate(-3deg);
  }
  .camp-times {
    position: absolute;
    left: 262px;
    top: 196px;
    width: 420px;
    height: 40px;
    line-height: 40px;
    background: var(--pink);
    border-radius: 6px;
    transform: rotate(-3deg);
    text-align: center;
    font-family: "Arimo", sans-serif;
    font-weight: 700;
    font-size: 24px;
    color: var(--white);
  }
  .gallery-note {
    position: absolute;
    left: 800px;
    top: 535px;
    width: 270px;
    margin: 0;
    text-align: center;
    font-family: "Arimo", sans-serif;
    font-size: 25px;
    line-height: 33px;
    color: var(--white);
    transform: translate(-50%, -50%) rotate(-32deg);
  }
  .tagline {
    position: absolute;
    right: 50px;
    top: 738px;
    margin: 0;
    text-align: right;
    font-family: "Roboto Condensed", sans-serif;
    font-weight: 400;
    font-size: 62px;
    line-height: 64px;
    color: var(--pink);
  }
  .camp-details {
    position: absolute;
    right: 50px;
    top: 882px;
    width: 430px;
    text-align: right;
    font-family: "Arimo", sans-serif;
    font-size: 19px;
    line-height: 25px;
    color: var(--ink);
  }
  .camp-details p {
    margin: 0 0 18px 0;
  }
  .brand {
    position: absolute;
    left: 37px;
    top: 737px;
    width: 300px;
    height: 300px;
    display: flex;
    align-items: center;
    justify-content: center;
    gap: 10px;
  }
  .brand-dot {
    width: 24px;
    height: 24px;
    border-radius: 50%;
    background: var(--sky-deep);
  }
  .brand-name {
    font-family: "Arimo", sans-serif;
    font-size: 32px;
    color: var(--sky-deep);
  }
  .contact-band {
    position: absolute;
    left: 0;
    right: 0;
    top: 1080px;
    height: 64px;
    line-height: 64px;
    background: var(--pink);
    text-align: center;
    font-family: "Arimo", sans-serif;
    font-size: 23px;
    color: var(--white);
  }
</style>
</head>
<body>
<main class="flyer">
  <svg class="flyer-shapes" width="964" height="1200" viewBox="0 0 964 1200" xmlns="http://www.w3.org/2000/svg">
    <defs>
      <radialGradient id="sky-rays" cx="0.45" cy="0.15" r="0.8">
        <stop offset="0" stop-color="#eaf8fe"/>
        <stop offset="0.5" stop-color="#a5dcf4"/>
        <stop offset="1" stop-color="#5bbbe8"/>
      </radialGradient>
      <linearGradient id="kids-tones" x1="0" y1="0" x2="0" y2="1">
        <stop offset="0" stop-color="#d8c0b6" stop-opacity="0"/>
        <stop offset="0.25" stop-color="#d9a08e"/>
        <stop offset="0.55" stop-color="#b8454a"/>
        <stop offset="0.8" stop-color="#3b4f9a"/>
        <stop offset="1" stop-color="#ece8ef"/>
      </linearGradient>
      <clipPath id="photo-clip">
        <circle cx="380" cy="310" r="362"/>
      </clipPath>
    </defs>

    <rect class="backdrop" width="964" height="1200" fill="var(--sky)"/>
    <circle class="deco-ring" cx="40" cy="830" r="250" fill="none" stroke="#55b7e8" stroke-width="40" opacity="0.6"/>
    <circle class="deco-ring" cx="860" cy="560" r="330" fill="none" stroke="var(--sky-ring)" stroke-width="30" opacity="0.5"/>
    <circle class="deco-disc" cx="70" cy="1040" r="120" fill="var(--sky-ring)" opacity="0.4"/>

    <circle class="photo-frame" cx="380" cy="310" r="378" fill="var(--white)"/>
    <circle class="photo-sky" cx="380" cy="310" r="362" fill="url(#sky-rays)"/>
    <rect class="photo-area" role="img" aria-label="Photo of smiling children in party costumes with balloons"
          x="18" y="330" width="724" height="345" fill="url(#kids-tones)" clip-path="url(#photo-clip)"/>

    <circle class="info-circle-ring" cx="860" cy="976" r="432" fill="var(--white)"/>
    <circle class="info-circle" cx="860" cy="976" r="418" fill="var(--sky-pale)"/>

    <circle class="gallery-badge-ring" cx="800" cy="535" r="164" fill="var(--white)"/>
    <circle class="gallery-badge" cx="800" cy="535" r="152" fill="var(--green)"/>
    <circle class="gallery-badge-dots" cx="800" cy="535" r="134" fill="none" stroke="var(--white)" stroke-width="4" stroke-dasharray="1 9" stroke-linecap="round"/>

    <circle class="brand-ring" cx="187" cy="887" r="150" fill="var(--pink)"/>
    <circle class="brand-disc" cx="187" cy="887" r="128" fill="var(--white)"/>

    <path class="footer-curve" d="M520 1200 Q760 1150 964 1170 V1200 Z" fill="var(--white)"/>
  </svg>

  <h1 class="camp-title">Mid Term Camp</h1>
  <p class="camp-dates">26th - 30th of October</p>
  <div class="camp-times">9am - 3pm • 800 aed</div>

  <p class="gallery-note">Pixelnook<br>Camp photo gallery<br>updated daily!</p>

  <div class="brand">
    <span class="brand-dot"></span>
    <span class="brand-name">Wren Bloom</span>
  </div>

  <h2 class="tagline">Let your star<br>shine bright!</h2>
  <div class="camp-details">
    <p>Daily speech and confidence building classes, music &amp; movement, song, arts &amp; crafts, fine motor development and right brain training!</p>
    <p>Special performance of the Patchwork Fox from Quillby Theatre Group (Wednesday).</p>
  </div>

  <div class="contact-band">register@wrenbloom.ae or 043192764/ 0529316472 • www.wrenbloom.ae</div>
</main>
</body>
</html>
```